Lumorax Helpdesk overview brochure

Take the word document that is attached and turn it into a brochure. (Thinking one page, front and back.) the only existing branding/colors we have is the logo that is on the document. It may require a phone all or a bit of back and forth in text to explain some of the concepts in the attached document.

Target Market(s)

Call centers

Industry/Entity Type

It Service

Font styles to use
Sans Serif

Colors

Designer to choose colors to be used in the design.

Requirements
Must have
• A crisp professional look

```html
<!DOCTYPE html>
<html lang="en">
<head>
<meta charset="utf-8">
<title>Lumorax Helpdesk – Overview Brochure</title>
<link href="https://fonts.googleapis.com/css2?family=Lato:wght@300;400;700&display=swap" rel="stylesheet">
<style>
:root{
  --stage:#474747;
  --paper:#ffffff;
  --navy:#1a1c5a;
  --navy-deep:#17184f;
  --blue:#1f6fc4;
  --sky:#36aee8;
  --ice:#7fd0f5;
  --brand:#3db3ec;
  --text:#ffffff;
}
*{box-sizing:border-box;margin:0;padding:0}
html,body{width:1200px;height:776px;overflow:hidden;background:var(--stage);font-family:"Lato",sans-serif;color:var(--text)}
.canvas{position:relative;width:1200px;height:776px}
.sheet{position:absolute;top:58px;width:512px;height:659px;background:var(--paper);box-shadow:0 2px 10px rgba(0,0,0,.35)}
.sheet--front{left:58px}
.sheet--back{left:630px}
.panel{position:absolute;left:8px;top:8px;width:497px;height:644px;overflow:hidden;
  background:linear-gradient(150deg,var(--navy) 0%,var(--navy) 18%,var(--blue) 50%,var(--sky) 80%,var(--ice) 100%)}
.panel__band{position:absolute;inset:0;background:linear-gradient(160deg,rgba(23,24,79,0) 0%,rgba(23,24,79,.55) 100%);clip-path:polygon(0 88%,100% 58%,100% 100%,0 100%)}
.sheet--front .panel__band{clip-path:polygon(0 66%,100% 88%,100% 100%,0 100%)}
.panel__sheen{position:absolute;inset:0;background:rgba(255,255,255,.06);clip-path:polygon(0 82%,100% 42%,100% 100%,0 100%)}
.sheet--front .panel__sheen{clip-path:polygon(0 72%,100% 52%,100% 100%,0 100%)}
.deco-ring{position:absolute;border-radius:50%;border:28px solid rgba(255,255,255,.08)}
.brand{position:absolute;left:30px;top:28px;display:flex;align-items:center;gap:14px}
.brand__mark{width:62px;height:62px;border-radius:50%;background:rgba(61,179,236,.25);border:3px solid var(--brand)}
.brand__name{font-weight:400;font-size:29px;line-height:28px;letter-spacing:1.5px;color:var(--brand);text-transform:uppercase}
.dots{position:absolute;display:flex;flex-direction:column;gap:4px}
.dots i{display:block;width:8px;height:8px;border-radius:50%;background:#fff}
.lead{position:absolute;right:32px;top:113px;width:360px;text-align:right;font-weight:700;font-size:14px;line-height:17px}
.body{position:absolute;left:33px;top:190px;width:310px;font-weight:300;font-size:8.3px;line-height:10.8px}
.body p{margin-bottom:10.5px}
.section-title{position:absolute;left:0;width:100%;text-align:center;font-size:12.5px;letter-spacing:.3px;font-weight:400}
.costs{position:absolute;left:80px;top:436px;display:flex;gap:24px;align-items:center}
.cost{display:flex;align-items:center;gap:8px;font-size:10px;line-height:13px}
.cost__icon{width:38px;height:38px;border-radius:50%;display:flex;align-items:center;justify-content:center}
.cost__icon--phone{background:var(--navy);border:2px solid #fff}
.cost__icon--chat{background:#fff}
.cost__price{font-weight:700;font-size:15px;line-height:14px;text-align:left}
.cost__price small{display:block;font-weight:400;font-size:7px}
.arrows{position:absolute;left:176px;top:488px;display:flex;gap:6px}
.caption{position:absolute;left:0;top:540px;width:100%;text-align:center;font-weight:700;font-size:11.5px;line-height:14.5px}
.channels{position:absolute;left:63px;top:574px;display:flex;gap:5px}
.channel{height:38px;width:39px;background:#fff;color:var(--blue);font-size:7px;font-weight:700;display:flex;align-items:center;justify-content:center;text-align:center;line-height:8px}
.channel--wide{width:66px;margin-left:3px}
.model-title{position:absolute;right:42px;top:103px;font-size:12px;letter-spacing:.3px}
.step{position:absolute;display:flex;align-items:center;gap:7px;font-size:14px;font-weight:400}
.step__num{width:17px;height:17px;border-radius:50%;background:rgba(255,255,255,.85);color:var(--blue);font-size:11px;font-weight:700;display:flex;align-items:center;justify-content:center}
.copy{position:absolute;font-weight:300;font-size:10px;line-height:14px}
.list{list-style:none;position:absolute;font-weight:300;font-size:10px;line-height:14.6px}
.list li::before{content:"• "}
.footer{position:absolute;left:0;bottom:0;width:100%;height:60px;background:var(--navy-deep);border-top:2px solid rgba(255,255,255,.7);display:flex;align-items:center;justify-content:center;gap:22px;font-size:11.5px;letter-spacing:.4px}
.footer span{display:flex;align-items:center;gap:7px}
</style>
</head>
<body>
<div class="canvas">

  <section class="sheet sheet--front">
    <div class="panel">
      <div class="panel__sheen"></div>
      <div class="panel__band"></div>
      <div class="deco-ring" style="left:370px;top:210px;width:220px;height:220px"></div>

      <div class="brand"><div class="brand__mark"></div><div class="brand__name">Lumorax<br>Helpdesk</div></div>
      <div class="dots" style="left:456px;top:22px">
        <i style="opacity:.15"></i><i style="opacity:.25"></i><i style="opacity:.35"></i><i style="opacity:.5"></i><i style="opacity:.65"></i><i style="opacity:.8"></i><i></i><i></i>
      </div>

      <p class="lead">Lumorax Helpdesk helps contact centers serve new customer access channels, improve customer service, and lower costs of operation.</p>

      <div class="body">
        <p>The huge popularity of social media and messaging is creating customer preferences to communicate with your company using SMS text messaging, Chatterly Messenger, Teamloop, Vocana, Homely Echo, Nestwise Home, and many other new channels.</p>
        <p>App fatigue has set in. Customers are weary of installing, updating and learning how to use mobile apps. Your customers want to communicate with you using their messaging service of choice or just talk into their smart phone, computer, Homely Echo or similar device.</p>
        <p>Sensible automation of customer interactions on these new channels can provide better service at even lower costs of operation.</p>
        <p>According to Corvane Research’s report, by 2020, 85% of customer interactions will be managed without a human.</p>
        <p>Using specific techniques, Lumorax Helpdesk will help you shift some traffic from higher cost telephone calls to lower cost messaging channels. Shaping your traffic into lower cost channels has great financial benefits.</p>
      </div>

      <h2 class="section-title" style="top:409px">EXISTING CHANNELS HAVE DIFFERENT COSTS</h2>

      <div class="costs">
        <div class="cost">
          <div class="cost__icon cost__icon--phone">
            <svg width="20" height="20" viewBox="0 0 24 24"><path fill="#fff" d="M6.6 10.8c1.4 2.8 3.8 5.1 6.6 6.6l2.2-2.2c.3-.3.7-.4 1-.2 1.1.4 2.3.6 3.6.6.6 0 1 .4 1 1V20c0 .6-.4 1-1 1C10.6 21 3 13.4 3 4c0-.6.4-1 1-1h3.5c.6 0 1 .4 1 1 0 1.3.2 2.5.6 3.6.1.3 0 .7-.2 1z"/></svg>
          </div>
          <div>Telephone call<br>with live agent</div>
          <div class="cost__price">$0.15<small>per min</small></div>
        </div>
        <div class="cost">
          <div class="cost__icon cost__icon--chat">
            <svg width="22" height="20" viewBox="0 0 24 22"><path fill="#1f6fc4" d="M3 2h18a2 2 0 0 1 2 2v10a2 2 0 0 1-2 2H9l-5 5v-5H3a2 2 0 0 1-2-2V4a2 2 0 0 1 2-2z"/></svg>
          </div>
          <div>Web chat with<br>live agent</div>
          <div class="cost__price">$0.03<small>per min</small></div>
        </div>
      </div>

      <div class="arrows">
        <svg width="170" height="34" viewBox="0 0 170 34">
          <g fill="#fff">
            <path opacity=".3" d="M5 0h10v18h6L10 32 -1 18h6z"/>
            <path opacity=".5" d="M32 0h10v18h6L37 32 26 18h6z"/>
            <path opacity=".7" d="M59 0h10v18h6L64 32 53 18h6z"/>
            <path d="M86 0h10v18h6L91 32 80 18h6z"/>
            <path opacity=".7" d="M113 0h10v18h6l-11 14-11-14h6z"/>
            <path opacity=".5" d="M140 0h10v18h6l-11 14-11-14h6z"/>
            <path opacity=".3" d="M165 0h4v18h1l-5 14-5-14h5z"/>
          </g>
        </svg>
      </div>

      <p class="caption">With these new channels, the cost is similar to webchat.<br>Carefully automated interactions are at an even lower cost</p>

      <div class="channels">
        <div class="channel">SMS</div>
        <div class="channel">Teamloop</div>
        <div class="channel">Homely Echo</div>
        <div class="channel">Pingo</div>
        <div class="channel">Chatterly</div>
        <div class="channel">WePost</div>
        <div class="channel">TalkApp</div>
        <div class="channel channel--wide">Nestwise Home</div>
      </div>
    </div>
  </section>

  <section class="sheet sheet--back">
    <div class="panel">
      <div class="panel__sheen"></div>
      <div class="panel__band"></div>
      <div class="deco-ring" style="left:330px;top:240px;width:240px;height:240px"></div>

      <div class="brand"><div class="brand__mark"></div><div class="brand__name">Lumorax<br>Helpdesk</div></div>
      <div class="dots" style="left:451px;top:14px">
        <i style="opacity:.15"></i><i style="opacity:.25"></i><i style="opacity:.4"></i><i style="opacity:.55"></i><i style="opacity:.7"></i><i style="opacity:.85"></i><i></i><i></i>
      </div>

      <h2 class="model-title">ENGAGEMENT MODEL</h2>

      <div class="step" style="right:42px;top:133px"><span class="step__num">1</span>Proposal</div>
      <p class="copy" style="right:42px;top:154px;width:320px;text-align:right">Lumorax Helpdesk provides a written proposal.&nbsp; The proposal will describe our engagement methodologies and costs.</p>

      <div class="step" style="left:35px;top:200px"><span class="step__num">2</span>Engagement</div>
      <p class="copy" style="left:35px;top:223px;width:400px">Lumorax Helpdesk will meet with all the relevant stake holders on site and gather information to identify:</p>
      <ul class="list" style="left:35px;top:256px">
        <li>Historical traffic patterns.</li>
        <li>Actual costs by channel</li>
        <li>Review marketing plans that may impact customer service</li>
        <li>Review product plans that may impact customer service.</li>
        <li>Explore competition landscape as it relates to customer service.</li>
        <li>Review the existing corporate data store, analytics and reporting</li>
        <li>Review the current plans, metrics and budgets for customer service support</li>
      </ul>

      <div class="dots" style="left:40px;top:390px;gap:4.2px">
        <i></i><i></i><i style="opacity:.9"></i><i style="opacity:.85"></i><i style="opacity:.75"></i><i style="opacity:.65"></i><i style="opacity:.55"></i><i style="opacity:.5"></i><i style="opacity:.4"></i><i style="opacity:.3"></i><i style="opacity:.2"></i><i style="opacity:.12"></i><i style="opacity:.08"></i><i style="opacity:.05"></i>
      </div>

      <div class="step" style="left:81px;top:384px"><span class="step__num">3</span>Transformation Report</div>
      <ul class="list" style="left:80px;top:407px">
        <li>Executive summary</li>
        <li>Cost analysis per contact by channel</li>
        <li>Traffic patterns by channel</li>
        <li>Probable impacts of product and marketing plans</li>
        <li>Recommendations for achieving competitive advantage through service</li>
        <li>Recommendations for new channel types</li>
        <li>Recommendations for traffic shaping</li>
        <li>Near and long-term options for sensible automation</li>
        <li>Technology recommendations for implementing new channels</li>
        <li>Projected financial impact of recommendations</li>
      </ul>

      <footer class="footer">
        <span>
          <svg width="16" height="16" viewBox="0 0 24 24"><circle cx="12" cy="12" r="12" fill="#fff"/><path fill="#17184f" d="M8.4 10.9c.9 1.8 2.4 3.3 4.3 4.3l1.4-1.4c.2-.2.4-.3.7-.2.7.2 1.5.4 2.3.4.4 0 .6.3.6.6v2.3c0 .4-.3.6-.6.6C11.2 17.5 6.5 12.8 6.5 6.9c0-.4.3-.6.6-.6h2.3c.4 0 .6.3.6.6 0 .8.1 1.6.4 2.3.1.3 0 .5-.2.7z"/></svg>
          555-014-2290
        </span>
        <span>
          <svg width="16" height="16" viewBox="0 0 24 24" fill="none" stroke="#fff" stroke-width="1.6"><circle cx="12" cy="12" r="10"/><ellipse cx="12" cy="12" rx="4.5" ry="10"/><path d="M2 12h20M4 7h16M4 17h16"/></svg>
          WWW.LUMORAXDESK.NET
        </span>
      </footer>
    </div>
  </section>

</div>
</body>
</html>
```